Business Card Design for CoreLeafHarmony

We need the new logo on a business card for 3 employees:
Norma Kepple, PhD, Advanced Instructor and Practitioner of PulseWeave Vitalis Practice (email: norma@coreleafharmony.example)
Ted Halloran, Business Manager (email: ted@coreleafharmony.example)
Rosa Pilgrew, Administrative Assistant (email: rosa@quillgrove.example)

Target Market(s)

healthcare professionals

Industry/Entity Type

Alternative Medicine

Contact Information for Business Card

Names, titles, emails (names, titles, emails are in project description), phone, address, website, with logo and tagline. See below for address, phone, website: 418 Fennick St, Bldg 12, Ste 307
Santa Cruz, CA 95060
831-555-0174
www.coreleafharmony.example
Tagline: Craft of Balance, Light of Renewal

Font styles to use
Other font styles liked:
• Gabriela

Colors
00a990
86cfc6
6b449b
b7a5cd
85abd2
abd036

Requirements
Must have
• Colors and style that match the logo design - shades such as blue, green, purple
• Compatible or same font as in the logo
Nice to have
• Nice if it goes with the theme of Norma's last business card - uploaded below
Should not have
• colors or style in conflict with the logo

```html
<!DOCTYPE html>
<html lang="en">
<head>
<meta charset="utf-8">
<title>CoreLeafHarmony Business Card</title>
<link href="https://fonts.googleapis.com/css2?family=Gabriela&family=Barlow:wght@400;500&display=swap" rel="stylesheet">
<style>
  :root {
    --stage: #3b3b3d;
    --blue-light: #2f74b8;
    --blue-deep: #0f4a90;
    --navy: #173f78;
    --green: #3cb54a;
    --brand-green: #7cc242;
    --brand-purple: #4a2a86;
    --paper: #f1f1f1;
    --paper-shade: #e2e2e2;
    --ink: #1b1b1b;
    --name-blue: #1d4f97;
    --white: #ffffff;
  }
  * { box-sizing: border-box; margin: 0; padding: 0; }
  html, body { width: 1200px; height: 1000px; overflow: hidden; }
  body {
    background: var(--stage);
    position: relative;
    font-family: "Gabriela", Georgia, serif;
  }
  .card {
    position: absolute;
    left: 250px;
    width: 700px;
    height: 400px;
    border-radius: 28px;
    overflow: hidden;
    box-shadow: 0 12px 30px rgba(0,0,0,0.45);
  }
  .card--front {
    top: 60px;
    background: linear-gradient(160deg, var(--blue-light) 0%, var(--blue-deep) 100%);
  }
  .card--back {
    top: 540px;
    background: linear-gradient(180deg, var(--paper) 0%, var(--paper-shade) 100%);
  }
  .brand {
    position: absolute;
    display: flex;
    align-items: center;
    gap: 22px;
  }
  .brand__dot {
    width: 110px;
    height: 110px;
    border-radius: 50%;
    flex: none;
  }
  .brand__name {
    font-family: "Gabriela", Georgia, serif;
    font-size: 46px;
    line-height: 1;
  }
  .card--front .brand { left: 110px; top: 110px; }
  .card--front .brand__dot { background: var(--brand-green); }
  .card--front .brand__name { color: var(--white); }
  .tagline {
    position: absolute;
    left: 0; right: 0;
    top: 290px;
    text-align: center;
    color: var(--white);
    font-size: 19px;
    letter-spacing: 0.5px;
    text-transform: uppercase;
  }
  .card--back .brand { left: 120px; top: 40px; }
  .card--back .brand__dot { background: var(--brand-green); }
  .card--back .brand__name { color: var(--brand-purple); }
  .person {
    position: absolute;
    left: 0; right: 0;
    top: 178px;
    text-align: center;
  }
  .person__name {
    color: var(--name-blue);
    font-size: 24px;
  }
  .person__title {
    color: var(--ink);
    font-size: 16px;
    margin-top: 4px;
  }
  .rule {
    position: absolute;
    left: 0; right: 0;
    top: 248px;
    height: 5px;
    background: var(--green);
  }
  .band {
    position: absolute;
    left: 0; right: 0;
    top: 256px;
    bottom: 0;
    background: var(--navy);
    color: var(--white);
    font-family: "Barlow", Arial, sans-serif;
  }
  .address {
    position: absolute;
    left: 60px;
    top: 38px;
    width: 270px;
    text-align: right;
    font-size: 18px;
    line-height: 1.5;
  }
  .divider {
    position: absolute;
    left: 355px;
    top: 24px;
    width: 2px;
    height: 100px;
    background: rgba(255,255,255,0.6);
  }
  .contacts {
    position: absolute;
    left: 380px;
    top: 24px;
    list-style: none;
    font-size: 18px;
  }
  .contacts li {
    display: flex;
    align-items: center;
    gap: 10px;
    height: 33px;
  }
  .contacts svg { width: 20px; height: 20px; flex: none; }
</style>
</head>
<body>
  <section class="card card--front">
    <div class="brand">
      <span class="brand__dot"></span>
      <span class="brand__name">CoreLeafHarmony</span>
    </div>
    <p class="tagline">Craft of Balance, Light of Renewal</p>
  </section>

  <section class="card card--back">
    <div class="brand">
      <span class="brand__dot"></span>
      <span class="brand__name">CoreLeafHarmony</span>
    </div>
    <div class="person">
      <p class="person__name">Norma Kepple</p>
      <p class="person__title">PhD, Advanced Instructor and Practitioner</p>
    </div>
    <div class="rule"></div>
    <div class="band">
      <p class="address">418 Fennick St, Bldg 12,<br>Ste 307 Santa Cruz, CA 95060</p>
      <div class="divider"></div>
      <ul class="contacts">
        <li>
          <svg viewBox="0 0 20 20" aria-hidden="true"><circle cx="10" cy="10" r="10" fill="#fff"/><path d="M7 5l2 2-1 1.5c.6 1.4 1.6 2.4 3 3L12.5 10l2 2-1.5 2C9.5 14 6 10.5 6 6.5z" fill="#173f78"/></svg>
          <span>831-555-0174</span>
        </li>
        <li>
          <svg viewBox="0 0 20 20" aria-hidden="true"><circle cx="10" cy="10" r="10" fill="#fff"/><rect x="5" y="6.5" width="10" height="7" fill="none" stroke="#173f78" stroke-width="1.3"/><path d="M5 6.5l5 4 5-4" fill="none" stroke="#173f78" stroke-width="1.3"/></svg>
          <span>norma@coreleafharmony.example</span>
        </li>
        <li>
          <svg viewBox="0 0 20 20" aria-hidden="true"><circle cx="10" cy="10" r="10" fill="#fff"/><circle cx="10" cy="10" r="5.5" fill="none" stroke="#173f78" stroke-width="1.2"/><ellipse cx="10" cy="10" rx="2.4" ry="5.5" fill="none" stroke="#173f78" stroke-width="1.2"/><path d="M4.5 10h11" stroke="#173f78" stroke-width="1.2"/></svg>
          <span>www.coreleafharmony.example</span>
        </li>
      </ul>
    </div>
  </section>
</body>
</html>
```